New Bottle Label for our Velmoris Grand Reserva Brandy

Graphic Design Brief
We need a new bottle label for our Brandy Gran Reserva that we want to bring to the market.
Please have a look at all our current bottles and labels and the feel of our company under www.velmoris-distill.ch. We would like the design to be still different to the rest - as it is not a whisky, not a fruit product, not a spirit like a gin, thus we need to create like a new family, but still fitting in with the rest of the products.
The bottle that we will be using for the brand is a different one than the one that we already have, the design of the bottle is attached with a document.
I have also attached a briefing in regards to Brandy in general for your information.
### 1. What is Brandy?
Brandy is a distilled spirit made from fermented wine or other fruit wines. It is traditionally aged in oak barrels, which gives it its characteristic color and rich flavor. The aging process in oak is essential for developing the aromas and quality of the brandy.
### 2. What is Brandy Reserva?
A Brandy labeled as "Reserva" has undergone a longer aging process, typically at least 2 to 3 years, in oak barrels. This aging gives the brandy a deeper, more complex flavor profile and a darker color. "Reserva" is often an indication of higher quality.
### 3. Who enjoys drinking Brandy?
Brandy is typically favored by those who appreciate a deep, rich tasting experience. This often includes older consumers who value the time-aged complexity of the spirit. However, Brandy is also gaining popularity among younger people, especially through cocktails and modern serving styles.
### 4. Why is Brandy trending?
Brandy is experiencing a resurgence as consumers increasingly value quality and artisanal production methods. Its versatility in cocktails and association with traditional, luxurious experiences have also contributed to its renewed popularity.
### 5. What colors would be associated with Brandy?
The typical colors associated with Brandy are warm gold, amber, and deep golden-brown tones. These colors reflect the aging process in oak barrels and the richness of the flavors. Other associated colors might include dark brown and mahogany.
### 6. What is important to customers when buying Brandy?
Customers care about the origin of the Brandy, the aging time, the quality of the ingredients, the production method, and the brand. They also pay attention to the prestige of the product and the authenticity of the production.
### 7. What is not important to customers when buying Brandy?
For many customers, the price and packaging (unless it’s especially exclusive) may be less important than the quality and taste of the Brandy. The distillery name might be less significant if it isn’t tied to a particular reputation.
### 8. What do customers know about Swiss Brandy?
Swiss Brandy is still relatively unknown in many markets, but customers who are familiar with it appreciate the precision and quality of Swiss production. Swiss Brandy is assumed to be made with care and under strict quality standards.
### 9. What is Brandy Gran Reserva?
**Brandy Gran Reserva** is an even higher quality and longer-aged version of Brandy. Generally, a Gran Reserva is aged for at least 5 to 10 years or more in oak barrels. This extended aging process gives the Brandy an especially deep, complex flavor profile and often a darker, richer color. Gran Reserva is often regarded as the top-tier product within a Brandy range and appeals to discerning consumers who value quality, refinement, and a luxurious tasting experience.
The label “Gran Reserva” thus indicates the highest quality level for Brandies, similar to other spirits (like wine or whisky), where the aging time is a critical factor.
We age our Brandy Gran Reserva in the Solara way.
### 10. What emotions are associated with Brandy?
Brandy is often associated with luxury, relaxation, and comfort. It evokes feelings of tradition, elegance, and sophistication. Drinking Brandy is frequently seen as a moment of reflection and enjoyment.
### 11. How should Brandy be marketed?
Brandy should be marketed with a focus on its artisanal production, quality, and tradition. A narrative around the product, its aging, and origin can help create an emotional connection with the customer. The marketing should also emphasize the versatility of Brandy, whether consumed neat or in cocktails.
**Label design**:
The label should reflect the exclusivity of the product, with an elegant, minimalist design. The label should include information about the aging time, the use of oak barrels, and a brief story about the Brandy’s production.
we would like to have a modern look to the whole deisgn of the brandy
Customers that like Brandy
Switzerland
Distillery

```html
<!DOCTYPE html>
<html lang="en">
<head>
<meta charset="utf-8">
<title>Velmoris Grand Reserva Brandy – Label</title>
<link href="https://fonts.googleapis.com/css2?family=Roboto+Slab:wght@400;700&display=swap" rel="stylesheet">
<style>
  :root {
    --backdrop: #242424;
    --label-black: #000000;
    --gold-light: #f3d79a;
    --gold: #d2a862;
    --gold-deep: #8d6a33;
    --gold-solid: #c9a05c;
  }
  * { margin: 0; padding: 0; box-sizing: border-box; }
  html, body {
    width: 1200px; height: 1000px; overflow: hidden;
    background: var(--backdrop);
  }
  .canvas { position: relative; width: 1200px; height: 1000px; }
  .label {
    position: absolute; left: 200px; top: 100px;
    width: 800px; height: 800px;
    background: var(--label-black);
    box-shadow: 0 12px 36px rgba(0,0,0,.5);
  }
  .label__art { position: absolute; inset: 0; display: block; }
  .label__art text { font-family: "Roboto Slab", Georgia, serif; }
  .brand-name { font-weight: 700; font-size: 40px; fill: var(--gold-solid); }
  .brand-sub { font-weight: 400; font-size: 15px; letter-spacing: 1.5px; fill: var(--gold-solid); }
  .title { font-weight: 700; }
  .title--grand { font-size: 104px; }
  .title--reserva { font-size: 80px; }
  .title--brandy { font-size: 90px; }
  .vintage { font-weight: 400; font-size: 60px; letter-spacing: 1px; }
  .ornament {
    position: absolute; border-radius: 40%;
    background: radial-gradient(ellipse at center, rgba(210,168,98,.35), rgba(141,106,51,.08));
  }
</style>
</head>
<body>
<main class="canvas">
  <section class="label" aria-label="Velmoris Grand Reserva Brandy bottle label">
    <div class="ornament" role="img" aria-label="Gold scroll flourish, upper left" style="left:150px;top:175px;width:90px;height:48px;"></div>
    <div class="ornament" role="img" aria-label="Gold scroll flourish, upper right" style="left:560px;top:175px;width:90px;height:48px;"></div>
    <div class="ornament" role="img" aria-label="Gold scroll flourish, left side" style="left:62px;top:280px;width:100px;height:200px;"></div>
    <div class="ornament" role="img" aria-label="Gold scroll flourish, right side" style="left:638px;top:280px;width:100px;height:200px;"></div>
    <div class="ornament" role="img" aria-label="Gold scroll flourish, lower left" style="left:150px;top:568px;width:100px;height:50px;"></div>
    <div class="ornament" role="img" aria-label="Gold scroll flourish, lower right" style="left:550px;top:568px;width:100px;height:50px;"></div>

    <svg class="label__art" viewBox="0 0 800 800" width="800" height="800">
      <defs>
        <linearGradient id="goldStroke" x1="0" y1="0" x2="1" y2="1">
          <stop offset="0" stop-color="#f3d79a"/>
          <stop offset=".5" stop-color="#c9a05c"/>
          <stop offset="1" stop-color="#8d6a33"/>
        </linearGradient>
        <linearGradient id="goldText" x1="0" y1="0" x2="0" y2="1">
          <stop offset="0" stop-color="#f3d79a"/>
          <stop offset=".5" stop-color="#d2a862"/>
          <stop offset="1" stop-color="#8d6a33"/>
        </linearGradient>
      </defs>

      <g class="frame" fill="none" stroke="url(#goldStroke)" aria-hidden="true">
        <path stroke-width="6" d="M95,234 C100,190 170,170 230,150 C270,10 530,10 570,150 C630,170 700,190 705,234"/>
        <path stroke-width="2.5" d="M125,226 C130,196 188,182 242,166 C282,24 518,24 558,166 C612,182 670,196 675,226"/>
        <line x1="0" y1="228" x2="800" y2="228" stroke-width="2.5"/>
        <line x1="0" y1="241" x2="800" y2="241" stroke-width="6"/>

        <line x1="0" y1="536" x2="370" y2="536" stroke-width="6"/>
        <line x1="430" y1="536" x2="800" y2="536" stroke-width="6"/>
        <line x1="0" y1="549" x2="370" y2="549" stroke-width="2.5"/>
        <line x1="430" y1="549" x2="800" y2="549" stroke-width="2.5"/>
        <path stroke-width="2.5" d="M125,556 C130,590 188,604 242,620 C282,792 518,792 558,620 C612,604 670,590 675,556"/>
        <path stroke-width="6" d="M95,550 C100,600 170,620 230,640 C270,800 530,800 570,640 C630,620 700,600 705,550"/>
      </g>

      <g class="swiss-mark" aria-hidden="true">
        <rect x="378" y="532" width="44" height="44" fill="url(#goldStroke)"/>
        <rect x="396" y="541" width="8" height="26" fill="#000"/>
        <rect x="387" y="550" width="26" height="8" fill="#000"/>
      </g>

      <text class="brand-name" x="400" y="112" text-anchor="middle">Velmoris</text>
      <text class="brand-sub" x="400" y="140" text-anchor="middle">SWISS</text>
      <text class="brand-sub" x="400" y="162" text-anchor="middle">DISTILLERY</text>

      <text class="title title--grand" x="400" y="347" text-anchor="middle" fill="url(#goldText)">GRAND</text>
      <text class="title title--reserva" x="400" y="424" text-anchor="middle" fill="url(#goldText)">RESERVA</text>
      <text class="title title--brandy" x="400" y="502" text-anchor="middle" fill="url(#goldText)">BRANDY</text>

      <text class="vintage" x="400" y="708" text-anchor="middle" fill="url(#goldText)">2001</text>
    </svg>
  </section>
</main>
</body>
</html>
```